New web design for a service provider in the medical field

We are looking for a new design for our website. We are a company that repairs and sells medical endoscopes. Our customers include doctors and hospitals. Our current website can be found at https://lumenfix.example/en/lumenfix-english.
We need a new web design (without programming) for the following 3 pages:
-Startpage https://lumenfix.example/en/lumenfix-english/
-Used endoscopes https://lumenfix.example/en/used-endoscopes/
-Purchase https://lumenfix.example/en/purchase/
The design should be modern and stylish.
The blue color of the logo should be reflected on the page, but not too intrusive.
I have uploaded the images from the header. If more images are needed, let me know and I will upload them.

Target Market(s)
Doctors and hospitals

```html
<!DOCTYPE html>
<html lang="en">
<head>
<meta charset="utf-8">
<title>lumenFIX – Endoscope repair and sale</title>
<link href="https://fonts.googleapis.com/css2?family=Montserrat:wght@400;500;600;700;800&family=Open+Sans:wght@400;600&display=swap" rel="stylesheet">
<style>
:root{
  --navy:#1e3246;
  --navy-deep:#172838;
  --navy-soft:#2a4259;
  --blue:#1ea5e9;
  --blue-dark:#1584c2;
  --grey-bg:#eef1f4;
  --grey-line:#dde3e9;
  --text:#3c4a57;
  --muted:#7f8c98;
  --white:#ffffff;
}
*{box-sizing:border-box;margin:0;padding:0}
html,body{width:1200px;height:4518px;overflow:hidden}
body{position:relative;background:var(--white);font-family:"Open Sans",Arial,sans-serif;color:var(--text);font-size:14px;line-height:1.6}
h1,h2,h3,h4,.btn,.nav,.tab,.brand{font-family:"Montserrat",Arial,sans-serif}
.abs{position:absolute}
.btn{display:inline-block;background:var(--blue);color:var(--white);font-size:12px;font-weight:700;letter-spacing:1px;padding:13px 28px;border-radius:3px;text-transform:uppercase;white-space:nowrap}
.section-title{text-align:center;font-size:30px;font-weight:800;color:var(--navy);text-transform:uppercase}
.section-title::after{content:"";display:block;width:60px;height:4px;background:var(--blue);margin:14px auto 0}
.photo{border-radius:6px}

/* hero */
.hero{left:0;top:0;width:1200px;height:700px;overflow:hidden}
.brand{font-weight:700;font-size:24px;color:var(--white);display:flex;align-items:center;gap:10px;white-space:nowrap}
.brand .dot{width:14px;height:14px;border-radius:50%;background:var(--blue)}
.nav{left:380px;top:50px;width:780px;display:flex;justify-content:space-between;font-size:11px;font-weight:600;color:var(--white);text-transform:uppercase;white-space:nowrap}
.topcontact{right:40px;top:14px;display:flex;gap:22px;font-size:11px;color:#cfe3f2;white-space:nowrap}
.topcontact span{display:flex;align-items:center;gap:6px}
.hero h1{left:80px;top:175px;width:620px;font-size:40px;line-height:1.2;color:var(--white);font-weight:500;text-transform:uppercase}
.hero h1 b{font-weight:800}
.hero p{left:80px;top:290px;width:420px;color:#c8d7e4;font-size:14px}
.hero .btn{left:80px;top:380px}
.hero-photo{left:730px;top:95px;width:390px;height:460px;border-radius:12px;background:radial-gradient(circle at 55% 40%,#e9eef2 0%,#c9d3dc 45%,#2a4259 90%)}

/* service */
.service-title{left:0;top:710px;width:1200px}
.service-intro{left:260px;top:790px;width:680px;text-align:center;font-size:13px;color:var(--muted)}
.service-photo{left:200px;top:890px;width:300px;height:320px}
.service-text{left:540px;top:930px;width:440px}
.service-text h3{font-size:22px;font-weight:700;color:var(--navy);line-height:1.3;margin-bottom:18px}
.service-text p{font-size:13px;color:var(--muted);margin-bottom:12px}

/* brands & offers */
.offers{left:0;top:1300px;width:1200px;height:620px;background:var(--grey-bg)}
.tabs{left:190px;top:1380px;width:820px;display:flex;justify-content:space-between}
.tab{width:240px;height:62px;border-radius:31px;background:var(--white);display:flex;align-items:center;justify-content:center;font-weight:800;font-size:20px;color:var(--blue);letter-spacing:1px;box-shadow:0 6px 18px rgba(30,50,70,.08)}
.tab.active{background:var(--grey-line);color:var(--navy)}
.card{top:1510px;width:230px;height:370px;background:var(--white);border-radius:8px;overflow:hidden;box-shadow:0 10px 24px rgba(30,50,70,.1)}
.card .head{height:140px;position:relative}
.card .icon{position:absolute;left:85px;top:70px;width:60px;height:60px;border-radius:50%;background:var(--blue);display:flex;align-items:center;justify-content:center}
.card .body{padding:14px 22px;text-align:center}
.card h4{font-size:18px;color:var(--navy);font-weight:700}
.card h5{font-family:"Montserrat",sans-serif;font-size:11px;color:var(--blue);font-weight:600;margin-bottom:8px}
.card p{font-size:11.5px;color:var(--muted);line-height:1.55}
.card .link{margin-top:16px;font-family:"Montserrat",sans-serif;font-size:11px;font-weight:700;color:var(--navy);letter-spacing:.5px;border-top:1px solid var(--grey-line);padding-top:12px}

/* faulty */
.faulty{left:190px;top:2040px;width:420px}
.faulty h2{font-size:32px;font-weight:800;color:var(--navy)}
.faulty h4{font-size:15px;color:var(--blue);font-weight:700;margin:4px 0 16px}
.faulty p{font-size:13px;color:var(--muted);margin-bottom:22px}
.faulty-photo{left:650px;top:1960px;width:380px;height:380px;border-radius:50%}

/* outcome */
.outcome{left:0;top:2390px;width:1200px;height:770px;background:var(--navy)}
.outcome-title{left:0;top:2450px;width:1200px;text-align:center;color:var(--white);font-size:30px;font-weight:800}
.outcome-sub{left:330px;top:2500px;width:540px;text-align:center;font-size:12.5px;color:#a9bccd}
.tile{width:230px;height:250px;background:var(--white);border-radius:4px;overflow:hidden}
.tile .pic{height:150px}
.tile h4{font-size:11.5px;font-weight:700;color:var(--navy);text-align:center;margin:14px 12px 6px;text-transform:uppercase}
.tile p{font-size:11px;color:var(--muted);text-align:center;padding:0 16px;line-height:1.5}

/* decision */
.decision h2{left:0;top:3230px;width:1200px;text-align:center;font-size:28px;font-weight:800;color:var(--navy);text-transform:uppercase;line-height:1.35}
.benefit{width:240px;height:230px;background:var(--white);border-radius:6px;box-shadow:0 10px 28px rgba(30,50,70,.1);text-align:center;padding:26px 14px}
.benefit .icon{width:50px;height:50px;border-radius:50%;background:var(--blue);margin:0 auto 16px;display:flex;align-items:center;justify-content:center}
.benefit h4{font-size:15px;font-weight:700;color:var(--navy);margin-bottom:8px;white-space:nowrap}
.benefit p{font-size:11.5px;color:var(--muted);line-height:1.55;padding:0 6px}
.decision .btn{left:495px;top:3960px}

/* footer */
.footer-bg{left:0;top:4020px;width:1200px;height:498px}
.help{left:0;top:4200px;width:1200px;text-align:center;color:var(--white);font-size:28px;font-weight:800}
.help-btn{left:515px;top:4255px}
.fcol{top:4350px;width:160px;font-size:11px;color:#aebfce;line-height:1.8}
.fcol h5{font-family:"Montserrat",sans-serif;color:var(--white);font-size:12px;font-weight:700;margin-bottom:6px;text-transform:uppercase}
.fbrand{left:800px;top:4350px;width:260px}
.fbrand p{font-size:11px;color:#aebfce;margin-top:8px;line-height:1.6}
.social{display:flex;gap:10px;margin-top:12px}
.social i{width:26px;height:26px;border-radius:50%;background:var(--navy-soft);display:block}
.bottombar{left:0;top:4478px;width:1200px;height:40px;background:var(--navy-deep);display:flex;justify-content:space-between;align-items:center;padding:0 150px;font-size:11px;color:#8ea3b6}
</style>
</head>
<body>

<section class="abs hero">
  <svg class="abs" style="left:0;top:0" width="1200" height="700" viewBox="0 0 1200 700" aria-hidden="true">
    <rect width="1200" height="700" fill="#ffffff"/>
    <path d="M0 0H1200V560C1000 640 760 520 520 600C340 660 150 600 0 640Z" fill="#1e3246"/>
    <path d="M0 640C150 600 340 660 520 600C760 520 1000 640 1200 560V585C1000 665 760 548 520 628C340 688 150 628 0 668Z" fill="#1ea5e9"/>
    <path d="M600 0H1200V300C1050 220 860 260 700 160C640 120 610 60 600 0Z" fill="#2a4259" opacity=".7"/>
  </svg>
  <div class="abs brand" style="left:60px;top:36px"><span class="dot"></span>lumenFIX</div>
  <div class="abs topcontact">
    <span><svg width="12" height="12" viewBox="0 0 24 24"><path d="M6.6 10.8a15 15 0 006.6 6.6l2.2-2.2a1 1 0 011-.25 11 11 0 003.6.6 1 1 0 011 1V20a1 1 0 01-1 1A17 17 0 013 4a1 1 0 011-1h3.5a1 1 0 011 1 11 11 0 00.6 3.6 1 1 0 01-.25 1z" fill="#1ea5e9"/></svg>+49 (0)30 555 0142</span>
    <span><svg width="12" height="12" viewBox="0 0 24 24"><path d="M3 5h18v14H3z" fill="none" stroke="#1ea5e9" stroke-width="2"/><path d="M3 5l9 8 9-8" fill="none" stroke="#1ea5e9" stroke-width="2"/></svg>hello@lumenfix.example</span>
  </div>
  <nav class="abs nav"><span>Home</span><span>About us</span><span>Endoscope Repair</span><span>Used Endoscopes</span><span>Endoscope Purchase</span><span>Endoscopy Accessories</span><span>Contact</span></nav>
  <h1 class="abs">Put your <b>endoscope</b><br>in <b>reliable</b> hands!</h1>
  <p class="abs">Careful repair, tested second hand scopes and fair purchase offers for practices and clinics – all from one reliable team.</p>
  <span class="abs btn">Contact us</span>
  <div class="abs hero-photo" role="img" aria-label="Smiling doctor in a white coat holding a black endoscope"></div>
</section>

<h2 class="abs section-title service-title">Your future – our service</h2>
<p class="abs service-intro">lumenFIX is your specialist for the repair and sale of flexible endoscopes from all leading makers. We combine decades of experience with fast, transparent service for every practice and clinic.</p>
<div class="abs photo service-photo" role="img" aria-label="Technician's gloved hands working on an endoscope" style="background:linear-gradient(160deg,#dfe6ec,#7d93a8 60%,#2a4259)"></div>
<div class="abs service-text">
  <h3>Endoscope repairs and second hand endoscopes from lumenFIX – cause the outcome matters!</h3>
  <p>lumenFIX is your specialist partner for the repair, sale and purchase of flexible endoscopes. Our trained technicians restore function and image quality quickly and reliably.</p>
  <p>As a long-standing partner of doctors and hospitals we keep downtime short, offer loan scopes during repairs and give honest advice on every device.</p>
</div>

<div class="abs offers"></div>
<div class="abs tabs">
  <div class="tab">ORVISTA</div>
  <div class="tab active">PENTREL</div>
  <div class="tab">FUJARO</div>
</div>

<div class="abs card" style="left:255px">
  <div class="head"><svg width="230" height="140" aria-hidden="true"><path d="M0 0H230V90C170 130 60 130 0 95Z" fill="#1e3246"/></svg>
    <div class="icon"><svg width="26" height="26" viewBox="0 0 24 24"><path d="M14.7 6.3a4 4 0 00-5 5L4 17l3 3 5.7-5.7a4 4 0 005-5l-2.5 2.5-2.5-.5-.5-2.5z" fill="#fff"/></svg></div></div>
  <div class="body"><h4>Repair</h4><h5>Fast repair of scopes</h5><p>Whatever the damage, our experts restore your endoscope to full function with tested parts.</p><div class="link">REPAIR REQUEST</div></div>
</div>
<div class="abs card" style="left:485px">
  <div class="head"><svg width="230" height="140" aria-hidden="true"><path d="M0 0H230V90C170 130 60 130 0 95Z" fill="#1e3246"/></svg>
    <div class="icon"><svg width="26" height="26" viewBox="0 0 24 24"><path d="M3 12l9-9h7v7l-9 9z" fill="none" stroke="#fff" stroke-width="2"/><circle cx="15.5" cy="8.5" r="1.5" fill="#fff"/></svg></div></div>
  <div class="body"><h4>Sale</h4><h5>Used endoscopes</h5><p>Checked second hand endoscopes with warranty, ready for use in your practice.</p><div class="link">REPAIR REQUEST</div></div>
</div>
<div class="abs card" style="left:715px">
  <div class="head"><svg width="230" height="140" aria-hidden="true"><path d="M0 0H230V90C170 130 60 130 0 95Z" fill="#1e3246"/></svg>
    <div class="icon"><svg width="26" height="26" viewBox="0 0 24 24"><path d="M3 4h3l2 11h11l2-8H7" fill="none" stroke="#fff" stroke-width="2"/><circle cx="9" cy="19" r="1.6" fill="#fff"/><circle cx="17" cy="19" r="1.6" fill="#fff"/></svg></div></div>
  <div class="body"><h4>Purchase</h4><h5>Sell your endoscope</h5><p>We buy your used or defective endoscopes at fair prices with quick payment.</p><div class="link">SELL SCOPE</div></div>
</div>

<div class="abs faulty">
  <h2>FAULTY ENDOSCOPE?</h2>
  <h4>We ensure quick and smooth repairs!</h4>
  <p>A broken endoscope stops your daily routine. Send us your device and our team checks it at once, gives you a clear quote and returns it fully working in the shortest time. A loan scope keeps you running meanwhile.</p>
  <span class="btn">Ask for repair</span>
</div>
<div class="abs faulty-photo" role="img" aria-label="Stressed doctor holding his head in front of a light blue backdrop" style="background:radial-gradient(circle at 50% 45%,#f1f5f8 0%,#cfe6f5 55%,#8fc9ec 100%)"></div>

<div class="abs outcome"></div>
<h2 class="abs outcome-title">CAUSE THE OUTCOME MATTERS!</h2>
<p class="abs outcome-sub">From first contact to final check we take care of every detail, so you can focus fully on your patients.</p>

<div class="abs tile" style="left:215px;top:2580px"><div class="pic" role="img" aria-label="Service staff on the phone" style="background:linear-gradient(135deg,#dce4ea,#8aa2b8)"></div><h4>One contact for everything</h4><p>A personal advisor for all your questions.</p></div>
<div class="abs tile" style="left:485px;top:2580px"><div class="pic" role="img" aria-label="Technician inspecting an endoscope" style="background:linear-gradient(135deg,#e4eaef,#7f98ae)"></div><h4>Experience guaranteed</h4><p>Many years of know-how in endoscopy.</p></div>
<div class="abs tile" style="left:755px;top:2580px"><div class="pic" role="img" aria-label="Endoscope on a clinic table" style="background:linear-gradient(135deg,#d9e2e9,#6f879d)"></div><h4>The product is in good hands</h4><p>Careful handling at every step.</p></div>
<div class="abs tile" style="left:215px;top:2860px"><div class="pic" role="img" aria-label="Clinic team in a meeting" style="background:linear-gradient(135deg,#e1e8ee,#8ba1b5)"></div><h4>Guaranteed service</h4><p>Warranty on all repairs and sales.</p></div>
<div class="abs tile" style="left:485px;top:2860px"><div class="pic" role="img" aria-label="Close view of endoscope optics" style="background:linear-gradient(135deg,#d7e0e8,#6c8499)"></div><h4>Quality not quantity</h4><p>Every device is tested in detail.</p></div>
<div class="abs tile" style="left:755px;top:2860px"><div class="pic" role="img" aria-label="Doctor with patient in examination room" style="background:linear-gradient(135deg,#e3e9ee,#8199ad)"></div><h4>Service for everyone</h4><p>For practices and hospitals alike.</p></div>

<section class="decision">
  <h2 class="abs">LumenFix GmbH, your decision<br>for your future</h2>
  <div class="abs benefit" style="left:225px;top:3370px"><div class="icon"><svg width="22" height="22" viewBox="0 0 24 24"><path d="M13 2L4 14h7l-1 8 9-12h-7z" fill="#fff"/></svg></div><h4>Fast repairs</h4><p>Short turnaround times thanks to our own workshop and parts in stock.</p></div>
  <div class="abs benefit" style="left:480px;top:3370px"><div class="icon"><svg width="22" height="22" viewBox="0 0 24 24"><path d="M4 12l5 5L20 6" fill="none" stroke="#fff" stroke-width="3"/></svg></div><h4>Highly cost efficient</h4><p>Fair prices and clear quotes without hidden costs for your practice.</p></div>
  <div class="abs benefit" style="left:735px;top:3370px"><div class="icon"><svg width="22" height="22" viewBox="0 0 24 24"><path d="M12 2a7 7 0 017 7c0 5-7 13-7 13S5 14 5 9a7 7 0 017-7z" fill="#fff"/><circle cx="12" cy="9" r="2.5" fill="#1ea5e9"/></svg></div><h4>On site service</h4><p>Our technicians visit your clinic for checks and quick advice.</p></div>
  <div class="abs benefit" style="left:225px;top:3640px"><div class="icon"><svg width="22" height="22" viewBox="0 0 24 24"><path d="M4 7h13l-3-3M20 17H7l3 3" fill="none" stroke="#fff" stroke-width="2.5"/></svg></div><h4>Loan equipment service</h4><p>Keep working with a loan endoscope while yours is in repair.</p></div>
  <div class="abs benefit" style="left:480px;top:3640px"><div class="icon"><svg width="22" height="22" viewBox="0 0 24 24"><circle cx="12" cy="12" r="8" fill="none" stroke="#fff" stroke-width="2.5"/><path d="M12 7v5l3 3" fill="none" stroke="#fff" stroke-width="2.5"/></svg></div><h4>Without a maintenance</h4><p>No fixed contracts needed – service exactly when you need it.</p></div>
  <div class="abs benefit" style="left:735px;top:3640px"><div class="icon"><svg width="22" height="22" viewBox="0 0 24 24"><path d="M12 3l2.7 5.6 6.1.8-4.4 4.3 1 6.1L12 17l-5.4 2.8 1-6.1-4.4-4.3 6.1-.8z" fill="#fff"/></svg></div><h4>First class service</h4><p>Friendly experts who answer fast and support you personally.</p></div>
  <span class="abs btn">Learn more about lumenFIX</span>
</section>

<svg class="abs footer-bg" width="1200" height="498" viewBox="0 0 1200 498" aria-hidden="true">
  <path d="M0 60C220 0 420 90 640 50C860 10 1020 40 1200 10V498H0Z" fill="#1ea5e9"/>
  <path d="M0 95C220 35 420 125 640 85C860 45 1020 75 1200 45V498H0Z" fill="#1e3246"/>
</svg>
<h2 class="abs help">HOW CAN WE HELP YOU?</h2>
<span class="abs btn help-btn">Send us a message</span>

<div class="abs fcol" style="left:150px"><h5>Quick links</h5>About us<br>Repair<br>Used scopes<br>Purchase</div>
<div class="abs fcol" style="left:350px"><h5>Other links</h5>Privacy policy<br>Terms of use<br>Imprint<br>Contact</div>
<div class="abs fcol" style="left:550px;width:200px"><h5>Contact us</h5>Lindenstraße 12, 10115 Berlin<br>+49 (0)30 555 0142<br>hello@lumenfix.example</div>
<div class="abs fbrand">
  <div class="brand" style="font-size:20px"><span class="dot"></span>lumenFIX</div>
  <p>Repair, sale and purchase of flexible endoscopes for doctors and hospitals.</p>
  <div class="social"><i></i><i></i><i></i></div>
</div>
<div class="abs bottombar"><span>Imprint · Privacy policy · Terms</span><span>© 2024 LumenFix GmbH. All rights reserved.</span></div>

</body>
</html>
```